Business Card Design

Copper Willow is a cabin in Gatlinburg, Tennessee, near the Pale Ridge Hollow National Park. When our cabin was built, there was one thing more important than any other--peace. The front of our cabin is surrounded by woods. It has a huge deck with a swing, Adirondack chairs, and a love seat for relaxation. The back deck has a hot tub, a large round glass table for cocktails or dinner, and because we left no stone unturned, we have a telescope for stargazing. There are two master suites, each have a private bath with a large jetted tub, seperate shower, flat screen TV, and a door that leads to the back deck.

Industry/Entity Type

Business

Contact Information for Business Card

Copper Willow Vacation Rentals, LLC
817 Harlow Brook Pl.
Ashby Falls, Ky 40999
Janet K. Wilcox, Owner/Manager
(270) 555.0184

```html
<!DOCTYPE html>
<html lang="en">
<head>
<meta charset="utf-8">
<title>Copper Willow Vacation Rentals — Business Card</title>
<link rel="stylesheet" href="https://fonts.googleapis.com/css2?family=Oswald:wght@400;500&display=swap">
<style>
  :root {
    --backdrop: #1c1d1f;
    --card: #f4f4f3;
    --ink: #4a4a4a;
    --teal: #3f7f93;
    --teal-deep: #24586a;
    --rule: #5a8ea0;
  }
  * { box-sizing: border-box; margin: 0; padding: 0; }
  html, body { width: 1200px; height: 871px; overflow: hidden; }
  body {
    background: var(--backdrop);
    font-family: "Oswald", sans-serif;
    display: flex;
    flex-direction: column;
    align-items: center;
    justify-content: center;
    gap: 44px;
  }
  .card {
    position: relative;
    width: 660px;
    height: 377px;
    background: var(--card);
    overflow: hidden;
  }
  .wordmark {
    color: var(--teal);
    font-weight: 500;
    letter-spacing: 2px;
    line-height: 1.15;
    text-align: center;
  }
  .wordmark .mark {
    display: block;
    width: 14px; height: 14px;
    border-radius: 50%;
    background: var(--teal);
    margin: 0 auto 12px;
  }
  /* back */
  .card-back { display: flex; align-items: center; justify-content: center; }
  .card-back .wordmark { font-size: 38px; }
  /* front */
  .card-front .wordmark {
    position: absolute;
    left: 40px; top: 120px;
    width: 250px;
    font-size: 24px;
  }
  .divider {
    position: absolute;
    left: 312px; top: 90px;
    width: 2px; height: 160px;
    background: var(--rule);
  }
  .contact {
    position: absolute;
    left: 338px; top: 100px;
    color: var(--ink);
  }
  .contact .name { font-size: 30px; font-weight: 500; letter-spacing: 2px; line-height: 1.2; }
  .contact .role { font-size: 16px; color: var(--teal); letter-spacing: 1.5px; margin-bottom: 8px; }
  .contact .line {
    display: flex; align-items: center; gap: 8px;
    font-size: 16px; letter-spacing: 1px; line-height: 1.7;
    white-space: nowrap;
  }
  .contact svg { width: 14px; height: 14px; fill: var(--teal-deep); flex: none; }
  .band {
    position: absolute;
    right: 0; bottom: 0;
    width: 58%; height: 40px;
    background: linear-gradient(90deg, var(--teal), var(--teal-deep));
  }
</style>
</head>
<body>
  <section class="card card-back">
    <div class="wordmark"><span class="mark"></span>Copper Willow<br>Vacation Rentals, LLC</div>
  </section>

  <section class="card card-front">
    <div class="wordmark"><span class="mark"></span>Copper Willow<br>Vacation Rentals, LLC</div>
    <div class="divider"></div>
    <div class="contact">
      <p class="name">Janet K. Wilcox</p>
      <p class="role">Owner/Manager</p>
      <p class="line">
        <svg viewBox="0 0 24 24" aria-hidden="true"><path d="M12 2a7 7 0 0 0-7 7c0 5 7 13 7 13s7-8 7-13a7 7 0 0 0-7-7zm0 9.5A2.5 2.5 0 1 1 12 6.5a2.5 2.5 0 0 1 0 5z"/></svg>
        817 Harlow Brook Pl. Ashby Falls, Ky 40999
      </p>
      <p class="line">
        <svg viewBox="0 0 24 24" aria-hidden="true"><path d="M6.6 10.8a15 15 0 0 0 6.6 6.6l2.2-2.2a1 1 0 0 1 1-.25 11.4 11.4 0 0 0 3.6.57 1 1 0 0 1 1 1V20a1 1 0 0 1-1 1A17 17 0 0 1 3 4a1 1 0 0 1 1-1h3.5a1 1 0 0 1 1 1c0 1.25.2 2.450.57 3.57a1 1 0 0 1-.25 1z"/></svg>
        (270) 555.0184
      </p>
    </div>
    <div class="band"></div>
  </section>
</body>
</html>
```